marla verstegen
chef
marla verstegen - Chef / Catering
Creative Brief
Use specific fonts
may mix logo font with another font, both must be free and downloadable
Simple
professional chef
none
marla@marlaverstegen.net
marlaverstegen.net
For the biz cards: on the flip side, my social media info: website: marlaverstegen.net twitter: @marlaverstegen facebook: facebook.com/marla.verstegen blog: www.ourfinaldinnertable.net I'd like to have the symbols rather than words for social media I would like to have a folded card for thank yous and notes on the back of the envelope place the logo, then underneath: 518 tuckaway st. denver, co 80219 I would like the theme of the stars in the logo to be pulled through the products
website: marlaverstegen.net twitter: @marlaverstegen facebook: facebook.com/marla.verstegen blog: ourfinaldinnertable.net

```html
<!DOCTYPE html>
<html lang="en">
<head>
<meta charset="utf-8">
<title>marla verstegen – stationery set</title>
<link href="https://fonts.googleapis.com/css2?family=Open+Sans:wght@400;700&display=swap" rel="stylesheet">
<style>
  :root{
    --brand-red:#c3252d;
    --brand-red-dark:#9d1a21;
    --swoosh-grey:#b9b9b9;
    --paper:#ffffff;
    --ink:#555555;
    --board:#3b3b3b;
    --board-light:#444444;
    --label:#bdbdbd;
  }
  *{box-sizing:border-box;margin:0;padding:0}
  html,body{width:1200px;height:446px;overflow:hidden}
  body{
    background:radial-gradient(ellipse at 50% 40%,var(--board-light),var(--board) 75%);
    font-family:"Open Sans",Arial,sans-serif;position:relative;color:var(--ink);
  }
  .piece{position:absolute;background:var(--paper);overflow:hidden;box-shadow:0 2px 6px rgba(0,0,0,.45)}
  .piece svg.shape{position:absolute;inset:0;width:100%;height:100%}
  .caption{position:absolute;font-size:6px;color:var(--label);text-align:center}
  .wordmark{position:absolute;font-weight:700;color:var(--brand-red);line-height:1;white-space:nowrap;letter-spacing:-.3px}
  .wordmark.on-red{color:var(--paper)}
  .tagline{position:absolute;font-size:5px;color:#888;white-space:nowrap}
  .tagline.on-red{color:#f3d3d5}
  .contact{position:absolute;font-size:4.6px;line-height:1.55;white-space:nowrap;color:var(--ink)}
  .contact.on-red{color:var(--paper)}
  .contact.right{text-align:right}
  .icon{display:inline-block;width:5px;height:5px;border-radius:50%;background:var(--brand-red);vertical-align:middle;margin-right:3px}
</style>
</head>
<body>

<!-- Business card A: red reverse -->
<div class="piece card card-back" style="left:29px;top:26px;width:180px;height:100px;background:var(--brand-red)">
  <svg class="shape" viewBox="0 0 180 100" preserveAspectRatio="none">
    <path d="M150 0 C120 35 125 70 150 100 L180 100 L180 0Z" fill="var(--paper)"/>
    <path d="M142 0 C112 35 117 70 142 100" fill="none" stroke="var(--swoosh-grey)" stroke-width="3"/>
  </svg>
  <div class="contact on-red" style="left:10px;top:10px">
    <b>marla verstegen</b><br>chef / catering<br>
    marlaverstegen.net<br>@marlaverstegen<br>facebook.com/marla.verstegen<br>ourfinaldinnertable.net
  </div>
</div>
<div class="caption" style="left:29px;top:130px;width:180px">Business Card Option 1A</div>

<!-- Business card B: front -->
<div class="piece card card-front" style="left:29px;top:176px;width:180px;height:100px;background:var(--brand-red)">
  <svg class="shape" viewBox="0 0 180 100" preserveAspectRatio="none">
    <path d="M0 0 L140 0 C115 30 118 70 145 100 L0 100Z" fill="var(--paper)"/>
    <path d="M150 0 C125 30 128 70 155 100" fill="none" stroke="var(--swoosh-grey)" stroke-width="3"/>
  </svg>
  <div class="wordmark" style="left:12px;top:38px;font-size:15px">marla verstegen</div>
  <div class="tagline" style="left:12px;top:56px">chef / catering</div>
  <div class="contact" style="left:12px;top:70px">marla@marlaverstegen.net · (303) 555-0147</div>
</div>
<div class="caption" style="left:29px;top:280px;width:180px">Business Card Option 1B</div>

<!-- Business card C: white -->
<div class="piece card card-white" style="left:29px;top:318px;width:180px;height:100px">
  <svg class="shape" viewBox="0 0 180 100" preserveAspectRatio="none">
    <path d="M0 88 C60 78 120 78 180 88 L180 100 L0 100Z" fill="var(--brand-red)"/>
    <path d="M0 84 C60 74 120 74 180 84" fill="none" stroke="var(--swoosh-grey)" stroke-width="1.5"/>
  </svg>
  <div class="wordmark" style="left:12px;top:16px;font-size:15px">marla verstegen</div>
  <div class="tagline" style="left:12px;top:34px">chef / catering</div>
  <div class="contact" style="left:12px;top:50px">
    <span class="icon"></span>(303) 555-0147<br><span class="icon"></span>marla@marlaverstegen.net
  </div>
  <div class="contact" style="left:100px;top:50px">
    <span class="icon"></span>marlaverstegen.net<br><span class="icon"></span>@marlaverstegen
  </div>
</div>
<div class="caption" style="left:29px;top:422px;width:180px">Business Card Option 1C</div>

<!-- Letterhead A -->
<div class="piece letterhead" style="left:230px;top:24px;width:288px;height:376px">
  <svg class="shape" viewBox="0 0 288 376" preserveAspectRatio="none">
    <path d="M0 350 C90 330 200 330 288 345 L288 376 L0 376Z" fill="var(--brand-red)"/>
    <path d="M0 344 C90 324 200 324 288 339" fill="none" stroke="var(--swoosh-grey)" stroke-width="2"/>
    <path d="M4 0 C-2 120 -2 250 4 340" fill="none" stroke="var(--swoosh-grey)" stroke-width="1.5"/>
  </svg>
  <div class="wordmark" style="left:22px;top:22px;font-size:16px">marla verstegen</div>
  <div class="tagline" style="left:22px;top:40px">chef / catering</div>
  <div class="contact right" style="right:22px;top:22px">(303) 555-0147<br>marla@marlaverstegen.net<br>marlaverstegen.net</div>
</div>
<div class="caption" style="left:230px;top:406px;width:288px">Letterhead Option 1A</div>

<!-- Letterhead B -->
<div class="piece letterhead" style="left:534px;top:24px;width:288px;height:376px">
  <svg class="shape" viewBox="0 0 288 376" preserveAspectRatio="none">
    <path d="M0 356 C90 340 200 340 288 352 L288 376 L0 376Z" fill="var(--brand-red)"/>
    <path d="M0 350 C90 334 200 334 288 346" fill="none" stroke="var(--swoosh-grey)" stroke-width="2"/>
  </svg>
  <div class="wordmark" style="left:22px;top:22px;font-size:16px">marla verstegen</div>
  <div class="tagline" style="left:22px;top:40px">chef / catering</div>
  <div class="contact right" style="right:22px;top:22px">(303) 555-0147<br>marla@marlaverstegen.net</div>
  <div class="contact on-red" style="left:0;right:0;top:362px;text-align:center">518 tuckaway st. denver, co 80219 · marlaverstegen.net</div>
</div>
<div class="caption" style="left:534px;top:406px;width:288px">Letterhead Option 1B</div>

<!-- Envelope back, red flap -->
<div class="piece envelope" style="left:840px;top:26px;width:336px;height:112px">
  <svg class="shape" viewBox="0 0 336 112" preserveAspectRatio="none">
    <path d="M0 0 L336 0 L336 50 C250 70 90 70 0 50Z" fill="var(--brand-red)"/>
    <path d="M0 56 C90 76 250 76 336 56" fill="none" stroke="var(--swoosh-grey)" stroke-width="2"/>
  </svg>
  <div class="wordmark on-red" style="left:0;right:0;top:12px;text-align:center;font-size:13px">marla verstegen</div>
  <div class="tagline on-red" style="left:0;right:0;top:30px;text-align:center">518 tuckaway st. denver, co 80219</div>
</div>

<!-- Envelope back, white flap -->
<div class="piece envelope" style="left:840px;top:146px;width:336px;height:112px">
  <svg class="shape" viewBox="0 0 336 112" preserveAspectRatio="none">
    <path d="M0 0 L168 70 L336 0" fill="none" stroke="#d6d6d6" stroke-width="1"/>
    <path d="M0 112 L130 55 M336 112 L206 55" fill="none" stroke="#e2e2e2" stroke-width="1"/>
  </svg>
  <div class="wordmark" style="left:14px;top:14px;font-size:11px">marla verstegen</div>
  <div class="tagline" style="left:14px;top:27px">518 tuckaway st. denver, co 80219</div>
</div>

<!-- Envelope front -->
<div class="piece envelope" style="left:840px;top:268px;width:336px;height:122px">
  <svg class="shape" viewBox="0 0 336 122" preserveAspectRatio="none">
    <path d="M0 100 C100 86 240 86 336 98 L336 122 L0 122Z" fill="var(--brand-red)"/>
    <path d="M0 94 C100 80 240 80 336 92" fill="none" stroke="var(--swoosh-grey)" stroke-width="2"/>
  </svg>
  <div class="wordmark" style="left:14px;top:14px;font-size:11px">marla verstegen</div>
  <div class="tagline" style="left:14px;top:27px">518 tuckaway st. denver, co 80219</div>
</div>
<div class="caption" style="left:840px;top:396px;width:336px">Envelope Option 1A</div>

</body>
</html>
```